Consulting Company needs business card design

We need a business card design for a new consulting and business solutions company based in Bermuda called Corvane Holdings Limited. Looking for a double sided business card with one side only including the company logo thats attached and the other including contact information. Logo contains blue and turquoise colors and is fine to be on both sides of the card.
Contact Information for Business Card
Corvane Holdings Limited
P.O. Box KR318
Pemberly KR LT
Bermuda
Name: Marcus Telford
Position: Director
Telephone: 1 441 732 4590
Email: mtelford@corvane.bm
Website: www.corvane.bm

```html
<!DOCTYPE html>
<html lang="en">
<head>
<meta charset="utf-8">
<title>Corvane Holdings Limited – Business Card</title>
<link rel="stylesheet" href="https://fonts.googleapis.com/css2?family=Roboto+Condensed:wght@700&family=Roboto:wght@400;500&display=swap">
<style>
  :root {
    --backdrop: #2b2b2b;
    --card-white: #f4f4f3;
    --brand-blue: #24a3d9;
    --brand-teal: #17b0ae;
    --ink: #3c3c3c;
    --rule: #4a4a4a;
    --white: #ffffff;
  }
  * { margin: 0; padding: 0; box-sizing: border-box; }
  html, body { width: 1200px; height: 960px; overflow: hidden; }
  body {
    background: var(--backdrop);
    font-family: "Roboto", Arial, sans-serif;
    position: relative;
  }
  .card {
    position: absolute;
    width: 600px;
    height: 342px;
    border-radius: 22px;
    overflow: hidden;
  }
  .card--front { left: 314px; top: 113px; background: var(--card-white); }
  .card--back { left: 311px; top: 472px; background: var(--brand-blue); }

  .brand {
    position: absolute;
    right: 32px;
    top: 50px;
    display: flex;
    align-items: center;
    gap: 10px;
  }
  .brand__dot {
    width: 40px; height: 40px; border-radius: 50%;
    background: var(--brand-blue);
  }
  .brand__name {
    font-family: "Roboto", Arial, sans-serif;
    font-weight: 500;
    font-size: 30px;
    letter-spacing: 1px;
    color: var(--brand-blue);
  }

  .person { position: absolute; left: 31px; top: 172px; }
  .person__name {
    font-family: "Roboto Condensed", "Arial Narrow", sans-serif;
    font-weight: 700;
    font-size: 21px;
    color: var(--brand-blue);
    text-transform: uppercase;
    line-height: 24px;
  }
  .person__role {
    font-family: "Roboto Condensed", "Arial Narrow", sans-serif;
    font-weight: 700;
    font-size: 15px;
    color: var(--brand-teal);
    text-transform: uppercase;
    line-height: 20px;
  }
  .divider {
    position: absolute; left: 31px; right: 32px; top: 224px;
    height: 1px; background: var(--rule);
  }
  .contact {
    position: absolute; left: 31px; top: 253px;
    list-style: none;
    font-size: 14px; color: var(--ink); line-height: 19px;
  }
  .contact__item { display: flex; align-items: center; gap: 8px; }
  .contact__icon { width: 13px; height: 13px; fill: var(--brand-blue); }
  .address {
    position: absolute; right: 32px; top: 236px;
    text-align: right; font-style: normal;
    font-size: 14px; color: var(--ink); line-height: 17.5px;
  }
  .footer-band { position: absolute; left: 0; bottom: 0; width: 600px; height: 34px; }
  .footer-band__web {
    position: absolute; right: 32px; bottom: 10px;
    font-size: 13px; letter-spacing: 2px; color: var(--white);
  }

  .back__name {
    position: absolute; left: 0; right: 0; top: 118px;
    text-align: center;
    font-weight: 500; font-size: 40px; letter-spacing: 2px;
    color: var(--white);
  }
  .back__tagline {
    position: absolute; left: 0; right: 0; top: 170px;
    text-align: center;
    font-weight: 500; font-size: 18px; letter-spacing: 4px;
    color: var(--white); text-transform: uppercase;
  }
  .back__web {
    position: absolute; left: 0; right: 0; top: 282px;
    text-align: center;
    font-size: 13px; letter-spacing: 10px;
    color: var(--white);
  }
</style>
</head>
<body>
  <section class="card card--front" aria-label="Business card front">
    <div class="brand">
      <span class="brand__dot"></span>
      <span class="brand__name">CORVANE</span>
    </div>

    <div class="person">
      <p class="person__name">Marcus Telford</p>
      <p class="person__role">Director</p>
    </div>
    <div class="divider"></div>

    <ul class="contact">
      <li class="contact__item">
        <svg class="contact__icon" viewBox="0 0 24 24"><path d="M6.6 10.8c1.4 2.8 3.8 5.1 6.6 6.6l2.2-2.2c.3-.3.7-.4 1-.2 1.1.4 2.3.6 3.6.6.6 0 1 .4 1 1V20c0 .6-.4 1-1 1C10.6 21 3 13.4 3 4c0-.6.4-1 1-1h3.5c.6 0 1 .4 1 1 0 1.3.2 2.5.6 3.6.1.3 0 .7-.2 1z"/></svg>
        <span>1 441 732 4590</span>
      </li>
      <li class="contact__item">
        <svg class="contact__icon" viewBox="0 0 24 24"><path d="M2 5h20v14H2z M3 6l9 7 9-7" fill="var(--brand-blue)"/><path d="M3 6l9 7 9-7" fill="none" stroke="#f4f4f3" stroke-width="1.6"/></svg>
        <span>mtelford@corvane.bm</span>
      </li>
    </ul>

    <address class="address">
      Corvane Holdings Limited<br>
      P.O. Box KR318<br>
      Pemberly KR LT, Bermuda
    </address>

    <svg class="footer-band" viewBox="0 0 600 34" aria-hidden="true">
      <rect x="0" y="20" width="343" height="14" fill="var(--brand-teal)"/>
      <polygon points="366,0 600,0 600,34 336,34" fill="var(--brand-blue)"/>
    </svg>
    <span class="footer-band__web">www.corvane.bm</span>
  </section>

  <section class="card card--back" aria-label="Business card back">
    <p class="back__name">CORVANE</p>
    <p class="back__tagline">Holdings Limited</p>
    <p class="back__web">www.corvane.bm</p>
  </section>
</body>
</html>
```